design a construction company business card

Design business card around our logo. Card must have all the typical info: name, title, address, phone, email, business name, etc. Somewhere on the card I would like to see our motto "Built on integrity... Inspired by commitment." Consider adding a splash of bright orange to the card to complement the blues and silvers/grays in the logo. We are open to metallic inks, textures, etc. We would like to see options on both light and dark backgrounds. The font in the logo is Euro Technic Extended Regular.

```html
<!DOCTYPE html>
<html lang="en">
<head>
<meta charset="utf-8">
<title>Harlow Builders – Business Card</title>
<link href="https://fonts.googleapis.com/css2?family=Michroma&family=Exo+2:ital,wght@0,300;0,400;1,600&display=swap" rel="stylesheet">
<style>
  :root {
    --page-bg: #e7e4e0;
    --navy-deep: #0f2270;
    --navy: #1a3590;
    --royal: #2a4aa8;
    --glass-light: #eef0f2;
    --glass-mid: #d6d9dd;
    --silver: #d9dde6;
    --silver-dim: #b9c0cf;
    --steel-dark: #3a3d45;
    --logo-navy: #16275f;
    --motto-silver: #c9cede;
  }
  html, body {
    margin: 0;
    padding: 0;
    width: 1200px;
    height: 970px;
    overflow: hidden;
    background: var(--page-bg);
  }
  .canvas {
    position: relative;
    width: 1200px;
    height: 970px;
  }
  .card {
    position: absolute;
    left: 80px;
    top: 190px;
    width: 1040px;
    height: 590px;
    border-radius: 28px;
    overflow: hidden;
    background: linear-gradient(160deg, var(--glass-light) 0%, var(--glass-mid) 60%, #e4e6e9 100%);
    box-shadow: 0 18px 40px rgba(0,0,0,0.18);
  }
  .card-panel {
    position: absolute;
    inset: 0;
    width: 1040px;
    height: 590px;
  }
  .contact-side {
    position: absolute;
    left: 62px;
    top: 86px;
    color: var(--silver);
    font-family: "Exo 2", sans-serif;
  }
  .holder-name {
    margin: 0;
    font-family: "Michroma", sans-serif;
    font-size: 27px;
    letter-spacing: 0.5px;
    color: #e3e6ee;
    line-height: 1.1;
  }
  .holder-title {
    margin: 2px 0 0;
    font-size: 28px;
    font-weight: 300;
    color: var(--silver);
  }
  .address {
    margin: 66px 0 0;
    font-size: 23px;
    font-weight: 300;
    line-height: 31px;
    letter-spacing: 0.6px;
    font-style: normal;
  }
  .contact-list {
    list-style: none;
    margin: 24px 0 0;
    padding: 0;
  }
  .contact-list li {
    display: flex;
    align-items: center;
    gap: 10px;
    height: 38px;
    font-size: 23px;
    font-weight: 300;
    letter-spacing: 0.5px;
  }
  .contact-list li.phone { font-size: 27px; }
  .contact-icon { width: 34px; height: 34px; flex: none; }
  .motto {
    margin: 30px 0 0;
    font-size: 23px;
    font-style: italic;
    font-weight: 600;
    letter-spacing: 1px;
    line-height: 33px;
    color: var(--motto-silver);
  }
  .brand {
    position: absolute;
    left: 590px;
    top: 255px;
    width: 380px;
    text-align: center;
    font-family: "Michroma", sans-serif;
    color: var(--logo-navy);
  }
  .brand-name {
    margin: 0;
    font-size: 44px;
    line-height: 1.1;
    letter-spacing: 2px;
  }
  .brand-sub {
    margin: 8px 0 0;
    font-size: 19px;
    letter-spacing: 1px;
  }
</style>
</head>
<body>
<main class="canvas">
  <section class="card" aria-label="Business card">
    <svg class="card-panel" viewBox="0 0 1040 590" aria-hidden="true">
      <defs>
        <linearGradient id="panelBlue" x1="0" y1="0" x2="1" y2="1">
          <stop offset="0" stop-color="#2443a3"/>
          <stop offset="0.45" stop-color="#122a80"/>
          <stop offset="1" stop-color="#1d3488"/>
        </linearGradient>
        <linearGradient id="edgeSilver" x1="0" y1="0" x2="0" y2="1">
          <stop offset="0" stop-color="#f4f5f8"/>
          <stop offset="0.5" stop-color="#9aa0ab"/>
          <stop offset="1" stop-color="#eef0f4"/>
        </linearGradient>
      </defs>
      <path d="M0 0 H545 Q440 295 545 590 H0 Z" fill="url(#panelBlue)"/>
      <path d="M545 0 Q440 295 545 590" fill="none" stroke="url(#edgeSilver)" stroke-width="7"/>
      <path d="M548 0 Q452 295 548 590" fill="none" stroke="var(--steel-dark)" stroke-width="3" opacity="0.7"/>
    </svg>

    <div class="contact-side">
      <h1 class="holder-name">JHON SMITH</h1>
      <p class="holder-title">Founder</p>
      <address class="address">PO BOX 123 your address<br>2nd street Melbourne</address>
      <ul class="contact-list">
        <li class="phone">
          <svg class="contact-icon" viewBox="0 0 34 34" aria-hidden="true">
            <circle cx="17" cy="17" r="15.5" fill="none" stroke="#c9cede" stroke-width="2"/>
            <circle cx="17" cy="17" r="12" fill="#8c93a6"/>
            <rect x="12" y="9" width="10" height="16" rx="2" fill="none" stroke="#1a2a6e" stroke-width="2"/>
          </svg>
          555 555 5555
        </li>
        <li class="email">
          <svg class="contact-icon" viewBox="0 0 34 34" aria-hidden="true">
            <circle cx="17" cy="17" r="15.5" fill="none" stroke="#c9cede" stroke-width="2"/>
            <circle cx="17" cy="17" r="12" fill="#8c93a6"/>
            <rect x="10" y="12" width="14" height="10" fill="none" stroke="#1a2a6e" stroke-width="2"/>
            <path d="M10 12 L17 18 L24 12" fill="none" stroke="#1a2a6e" stroke-width="2"/>
          </svg>
          Info@companygmail.com
        </li>
        <li class="web">
          <svg class="contact-icon" viewBox="0 0 34 34" aria-hidden="true">
            <circle cx="17" cy="17" r="15.5" fill="none" stroke="#c9cede" stroke-width="2"/>
            <circle cx="17" cy="17" r="12" fill="#8c93a6"/>
            <circle cx="17" cy="17" r="7.5" fill="none" stroke="#1a2a6e" stroke-width="1.8"/>
            <ellipse cx="17" cy="17" rx="3.2" ry="7.5" fill="none" stroke="#1a2a6e" stroke-width="1.5"/>
            <path d="M9.5 17 H24.5" stroke="#1a2a6e" stroke-width="1.5"/>
          </svg>
          www.companywebsite.com
        </li>
      </ul>
      <p class="motto">Built on integrity...<br>Inspired by commitment.</p>
    </div>

    <div class="brand">
      <p class="brand-name">HARLOW</p>
      <p class="brand-sub">BUILDERS, INC.</p>
    </div>
  </section>
</main>
</body>
</html>
```